10 Page Marketing Report Template - Cindermoor Care Allies

https://www.vidquill.example/share/7f1e9c04b2d84a61a5c3e9d02b6f4a17

We are creating a professional, modern, and slightly edgy PDF-style report document (about 10 pages) to showcase the results of a client’s first 30 days with Cindermoor Care Allies.

The report will be designed as a customizable Plakkit template so the Client Success team can easily update logos, screenshots, and text for each client.

This document will serve as both a visual presentation piece and a report deliverable, blending clean design, modern layout, and data-driven storytelling.

I am attaching the content for the report doc and the design brief along with the logo.
Here is our website for design style, look, and feel: https://cindermoorcare.example/

Here is a quick overview video I made:

```html
<!DOCTYPE html>
<html lang="en">
<head>
<meta charset="utf-8">
<title>30 Days to Value Report – Cindermoor Care Allies</title>
<link href="https://fonts.googleapis.com/css2?family=Poppins:ital,wght@0,400;0,500;0,600;0,700;1,400&display=swap" rel="stylesheet">
<style>
:root{
  --stage:#cacaca;
  --paper:#ffffff;
  --navy:#1f2a44;
  --teal:#164d6b;
  --gold:#fbb017;
  --ink:#222632;
  --muted:#e9e9ea;
  --muted-ink:#c4c4c4;
}
*{margin:0;padding:0;box-sizing:border-box}
html,body{width:696px;height:1200px;overflow:hidden;background:var(--stage)}
body{position:relative;font-family:'Poppins',sans-serif;color:var(--ink)}
.page{position:absolute;width:181px;height:255px;background:var(--paper);overflow:hidden}

/* cover */
.cover{left:258px;top:57px;width:180px;background:var(--navy)}
.cover-photo{position:absolute;inset:0;background:linear-gradient(180deg,#0f1524 0%,#1d2740 45%,#2e3c5e 100%)}
.cover-shape{position:absolute;inset:0}
.cover-brand{position:absolute;left:12px;top:20px;display:flex;gap:4px;align-items:flex-start}
.brand-square{width:7px;height:7px;background:var(--gold);margin-top:1px}
.cover-brand .brand-name{font-size:5.4px;line-height:6px;font-weight:600;color:var(--navy);letter-spacing:.3px}
.motto{position:absolute;left:12px;top:138px;font-size:6.6px;line-height:7.6px;font-weight:500;color:#fff}
.motto .gold{color:var(--gold);font-weight:700}
.cover-title{position:absolute;left:12px;top:172px;font-size:19px;line-height:20px;font-weight:600;color:#fff}
.cover-title .gold{color:var(--gold);font-weight:700}
.cover-sub{position:absolute;left:12px;top:214px;font-size:5px;font-weight:500;color:#fff}
.cover-meta{position:absolute;left:12px;top:233px;font-size:3.1px;line-height:6.4px;font-weight:500;color:#fff}

/* inner page furniture */
.page-brand{position:absolute;left:11px;top:9px;display:flex;gap:2px;align-items:flex-start}
.page-brand .brand-square{width:4px;height:4px;margin-top:.5px}
.page-brand .brand-name{font-size:2.6px;line-height:2.9px;font-weight:600;color:var(--navy);letter-spacing:.15px}
.heading{position:absolute;left:11px;font-size:7px;line-height:7.4px;font-weight:700;text-transform:uppercase}
.heading .accent{display:block;color:var(--gold)}
.heading .main{display:block;color:var(--navy)}
.sub{position:absolute;left:11px;font-size:4.6px;line-height:5px;font-weight:600;color:var(--gold);text-transform:uppercase}
.sub.case{text-transform:none}
.sub .main{color:var(--navy);display:block}
.body{position:absolute;left:11px;width:159px;font-size:3.3px;line-height:4.3px;color:var(--ink);text-align:justify}
.list{position:absolute;left:11px;list-style:none;font-size:3.3px;line-height:4.3px;color:var(--ink)}
.list li{position:relative;padding-left:5px;margin-bottom:3.2px}
.list li::before{content:"";position:absolute;left:1px;top:1.6px;width:1.1px;height:1.1px;border-radius:50%;background:var(--ink)}
.list.tight li{margin-bottom:2.2px}
.defs{position:absolute;left:11px;width:160px;font-size:3.3px;line-height:4.3px}
.defs p{margin-bottom:2.3px}
.defs b{font-weight:700}
.footer-title{position:absolute;left:11px;top:238px;font-size:2.9px;line-height:3.3px;font-weight:700;color:var(--navy)}
.footer-title .gold{color:var(--gold)}
.footer-mark{position:absolute;left:126px;top:236px;width:43px;height:19px}
.photo{position:absolute;left:11px;width:159px}
.photo-meeting{background:linear-gradient(120deg,#4b5563 0%,#b7c0c9 45%,#6b6f76 75%,#2f343c 100%)}
.photo-growth{background:linear-gradient(120deg,#3d444e 0%,#8d959f 50%,#55606b 100%)}
.photo-content{background:linear-gradient(135deg,#262a31 0%,#5c636c 55%,#3a3f46 100%)}
.placeholder{position:absolute;top:133px;width:77px;height:52px;background:var(--muted);display:flex;align-items:center;justify-content:center;font-size:2.8px;color:var(--muted-ink);letter-spacing:.2px}

/* devices */
.tablet{position:absolute;left:124px;top:80px;width:40px;height:56px;border:2px solid #15171c;border-radius:2px;background:#fff}
.laptop-screen{position:absolute;left:106px;top:148px;width:58px;height:38px;border:2px solid #15171c;border-radius:1.5px;background:#fff}
.laptop-base{position:absolute;left:100px;top:186px;width:70px;height:2px;border-radius:0 0 2px 2px;background:#b9bcc2}
.screen-brand{position:absolute;left:50%;top:50%;transform:translate(-50%,-50%);font-size:2px;line-height:2.3px;font-weight:600;color:var(--navy);text-align:center;white-space:nowrap}
.phone{position:absolute;top:99px;width:45px;height:88px;border:1.5px solid #d3d6dc;border-radius:4px;background:linear-gradient(160deg,#eef1ee 0%,#dfe9df 40%,#e8ecf2 100%)}
.phone-menu{background:linear-gradient(90deg,#ffffff 0%,#ffffff 72%,#dfe7de 100%)}
.illustration{position:absolute;left:105px;top:93px;width:65px;height:66px;border-radius:4px;background:radial-gradient(circle at 55% 55%,#e7ecf7 0%,#f6f8fc 60%,#ffffff 100%)}
.chart{position:absolute;left:11px;top:134px;width:160px;height:70px}
.closing{position:absolute;left:11px;width:160px;font-size:3.3px;line-height:4.3px}
.closing b{font-weight:700}
</style>
</head>
<body>

<section class="page cover">
  <div class="cover-photo" role="img" aria-label="Dim office interior with rising bar-chart columns behind a conference table"></div>
  <svg class="cover-shape" viewBox="0 0 180 255" preserveAspectRatio="none" aria-hidden="true">
    <path d="M0 0 H140 Q98 72 0 88 Z" fill="#ffffff"/>
    <path d="M140 0 H180 V5 Q118 82 0 93 V88 Q98 72 140 0 Z" fill="#fbb017"/>
  </svg>
  <div class="cover-brand">
    <span class="brand-square"></span>
    <div class="brand-name">CINDERMOOR<br>CARE<br>ALLIES</div>
  </div>
  <div class="motto">Live With Integrity.<br><span class="gold">Serve With Excellence.</span><br>Change The World.</div>
  <h1 class="cover-title">30 Days to<br><span class="gold">Value Report</span></h1>
  <div class="cover-sub">Cindermoor Care Allies</div>
  <div class="cover-meta">Client: [Client Name] &nbsp;&nbsp; Date: 22-11-2025<br>Prepared by: Cindermoor Care Allies</div>
</section>

<section class="page" style="left:57px;top:334px">
  <div class="page-brand"><span class="brand-square"></span><div class="brand-name">CINDERMOOR<br>CARE<br>ALLIES</div></div>
  <h2 class="heading" style="top:38px"><span class="accent">Welcome</span><span class="main">and Overview</span></h2>
  <p class="body" style="top:56px">The first 30 days are about creating momentum. Our goal was to build the foundation for measurable growth — from your website and Searchly Business Profile to your SEO systems, audits, and backlink strategy.</p>
  <div class="photo photo-meeting" style="top:74px;height:68px" role="img" aria-label="Business team shaking hands across a meeting table"></div>
  <p class="body" style="top:147px;font-style:italic">This report highlights what’s been accomplished and what’s next in your marketing journey.</p>
  <div class="footer-title">30 DAYS TO <span class="gold">VALUE REPORT</span><br>CINDERMOOR CARE ALLIES</div>
  <svg class="footer-mark" viewBox="0 0 43 19" aria-hidden="true"><path d="M0 0 H43 L25 19 H13 Q14 8 0 0 Z" fill="#fbb017"/></svg>
</section>

<section class="page" style="left:258px;top:334px">
  <div class="page-brand"><span class="brand-square"></span><div class="brand-name">CINDERMOOR<br>CARE<br>ALLIES</div></div>
  <h2 class="heading" style="top:38px"><span class="accent">Highlights</span><span class="main">and Quick Wins</span></h2>
  <ul class="list tight" style="top:58px">
    <li>Website launched and optimized for SEO</li>
    <li>Searchly Business Profiles verified and optimized</li>
    <li>Comprehensive SEO audits completed</li>
    <li>Backlink strategy implementation underway</li>
    <li>First blog articles published</li>
    <li>Tracking and analytics systems connected</li>
  </ul>
  <div class="photo photo-growth" style="top:103px;height:68px" role="img" aria-label="Hand sketching 2025 with rising arrows over a laptop"></div>
  <div class="footer-title">30 DAYS TO <span class="gold">VALUE REPORT</span><br>CINDERMOOR CARE ALLIES</div>
  <svg class="footer-mark" viewBox="0 0 43 19" aria-hidden="true"><path d="M0 0 H43 L25 19 H13 Q14 8 0 0 Z" fill="#fbb017"/></svg>
</section>

<section class="page" style="left:458px;top:334px">
  <div class="page-brand"><span class="brand-square"></span><div class="brand-name">CINDERMOOR<br>CARE<br>ALLIES</div></div>
  <h2 class="heading" style="top:38px"><span class="accent">Comprehensive Audits</span><span class="main">and Strategy Development</span></h2>
  <p class="body" style="top:56px">To ensure long-term results, our team conducted a full suite of technical and strategic audits during the first month. These insights guided your SEO roadmap and content strategy moving forward.</p>
  <div class="sub" style="top:76px">Audits and<span class="main">Deliverables Completed:</span></div>
  <div class="defs" style="top:89px">
    <p><b>Technical SEO Audit:</b> Site health, indexation, and crawl efficiency</p>
    <p><b>Backlink Audit:</b> Link quality, toxicity review, and authority scoring</p>
    <p><b>Competitor Analysis:</b> Top-ranking competitors’ content, backlinks, and keyword profiles</p>
    <p><b>On-Page SEO Audit:</b> Metadata, headings, internal links, and content structure</p>
    <p><b>Content Audit:</b> Keyword targeting, topical gaps, and conversion opportunities</p>
    <p><b>Strategy Development:</b> 90-day SEO plan and keyword roadmap created</p>
  </div>
  <div class="placeholder" style="left:11px">PLACE HOLDER</div>
  <div class="placeholder" style="left:93px">PLACE HOLDER</div>
  <div class="footer-title">30 DAYS TO <span class="gold">VALUE REPORT</span><br>CINDERMOOR CARE ALLIES</div>
  <svg class="footer-mark" viewBox="0 0 43 19" aria-hidden="true"><path d="M0 0 H43 L25 19 H13 Q14 8 0 0 Z" fill="#fbb017"/></svg>
</section>

<section class="page" style="left:57px;top:611px">
  <div class="page-brand"><span class="brand-square"></span><div class="brand-name">CINDERMOOR<br>CARE<br>ALLIES</div></div>
  <h2 class="heading" style="top:38px"><span class="accent">Website</span><span class="main">Progress</span></h2>
  <p class="body" style="top:56px">To ensure long-term results, our team conducted a full suite of technical and strategic audits during the first month. These insights guided your SEO roadmap and content strategy moving forward.</p>
  <div class="sub" style="top:82px">Launched Pages</div>
  <p class="body" style="top:88px;width:110px;text-align:left">[List live pages, e.g., Home, About, Services, Contact, etc.]</p>
  <div class="sub" style="top:114px">Optimizations Completed</div>
  <ul class="list tight" style="top:120px">
    <li>On-page SEO (titles, meta, H1s)</li>
    <li>Local schema added</li>
    <li>Call tracking integrated</li>
    <li>Mobile responsiveness reviewed</li>
  </ul>
  <div class="sub" style="top:171px">Next Steps</div>
  <ul class="list tight" style="top:177px">
    <li>CRO improvements</li>
    <li>Additional service or location pages</li>
  </ul>
  <div class="tablet"><div class="screen-brand">CINDERMOOR<br>CARE ALLIES</div></div>
  <div class="laptop-screen"><div class="screen-brand">CINDERMOOR<br>CARE ALLIES</div></div>
  <div class="laptop-base"></div>
  <div class="footer-title">30 DAYS TO <span class="gold">VALUE REPORT</span><br>CINDERMOOR CARE ALLIES</div>
  <svg class="footer-mark" viewBox="0 0 43 19" aria-hidden="true"><path d="M0 0 H43 L25 19 H13 Q14 8 0 0 Z" fill="#fbb017"/></svg>
</section>

<section class="page" style="left:258px;top:611px">
  <div class="page-brand"><span class="brand-square"></span><div class="brand-name">CINDERMOOR<br>CARE<br>ALLIES</div></div>
  <h2 class="heading" style="top:38px"><span class="accent">Searchly</span><span class="main">Business Profile</span></h2>
  <ul class="list tight" style="top:56px">
    <li>Profiles verified and optimized</li>
    <li>Categories, services, and photos updated</li>
    <li>Images updated and optimized for visibility and engagement</li>
    <li>Review strategy initiated</li>
    <li>Visibility and engagement tracking started</li>
  </ul>
  <div class="phone phone-menu" style="left:11px" role="img" aria-label="Phone screen showing the profile app menu"></div>
  <div class="phone" style="left:67px" role="img" aria-label="Phone screen showing a map with location pins"></div>
  <div class="phone" style="left:124px" role="img" aria-label="Phone screen showing the business listing card over a map"></div>
  <div class="footer-title">30 DAYS TO <span class="gold">VALUE REPORT</span><br>CINDERMOOR CARE ALLIES</div>
  <svg class="footer-mark" viewBox="0 0 43 19" aria-hidden="true"><path d="M0 0 H43 L25 19 H13 Q14 8 0 0 Z" fill="#fbb017"/></svg>
</section>

<section class="page" style="left:458px;top:611px">
  <div class="page-brand"><span class="brand-square"></span><div class="brand-name">CINDERMOOR<br>CARE<br>ALLIES</div></div>
  <h2 class="heading" style="top:38px"><span class="accent">Content</span><span class="main">and SEO</span></h2>
  <div class="photo photo-content" style="left:104px;top:37px;width:66px;height:51px" role="img" aria-label="Laptop with content marketing chart graphics"></div>
  <div class="sub" style="top:62px">Content Published</div>
  <p class="body" style="top:68px;width:90px;text-align:left">[List blog titles or link URLs here.]</p>
  <div class="sub" style="top:87px">SEO Progress</div>
  <ul class="list tight" style="top:93px;width:160px">
    <li>Initial keyword tracking launched</li>
    <li>On-page SEO and internal linking completed</li>
    <li>Foundational ranking movement observed (if applicable)</li>
    <li style="text-align:justify">Pillar &amp; Cluster Content Calendar created — outlining key topics, publishing cadence, and interlinking structure for long-term SEO growth</li>
  </ul>
  <div class="sub" style="top:137px">Next Steps</div>
  <ul class="list" style="top:143px">
    <li>Continue publishing cluster blogs weekly</li>
    <li>Begin interlinking to new service pages</li>
  </ul>
  <div class="footer-title">30 DAYS TO <span class="gold">VALUE REPORT</span><br>CINDERMOOR CARE ALLIES</div>
  <svg class="footer-mark" viewBox="0 0 43 19" aria-hidden="true"><path d="M0 0 H43 L25 19 H13 Q14 8 0 0 Z" fill="#fbb017"/></svg>
</section>

<section class="page" style="left:57px;top:888px">
  <div class="page-brand"><span class="brand-square"></span><div class="brand-name">CINDERMOOR<br>CARE<br>ALLIES</div></div>
  <h2 class="heading" style="top:38px"><span class="accent">Citation Listings</span><span class="main">and Backlink Strategy</span></h2>
  <div class="sub" style="top:62px">Optimizations Completed</div>
  <ul class="list tight" style="top:68px">
    <li>Core directories completed (Searchly, Findr, Orchard, Reviewly, etc.)</li>
    <li>Industry-specific and regional listings submitted</li>
    <li>NAP (Name–Address–Phone) consistency audit completed</li>
  </ul>
  <div class="sub" style="top:100px">Backlink Work:</div>
  <ul class="list tight" style="top:106px">
    <li>Foundational backlinks placed</li>
    <li>Tier-1 authority outreach plan initiated</li>
    <li>Competitor link gap opportunities identified</li>
  </ul>
  <div class="sub" style="top:136px">Next Steps:</div>
  <ul class="list tight" style="top:142px">
    <li>Continue monthly citation expansion</li>
    <li>Launch next wave of backlink outreach</li>
  </ul>
  <div class="illustration" role="img" aria-label="Isometric illustration of chess pieces beside colourful bar blocks and a report sheet"></div>
  <div class="footer-title">30 DAYS TO <span class="gold">VALUE REPORT</span><br>CINDERMOOR CARE ALLIES</div>
  <svg class="footer-mark" viewBox="0 0 43 19" aria-hidden="true"><path d="M0 0 H43 L25 19 H13 Q14 8 0 0 Z" fill="#fbb017"/></svg>
</section>

<section class="page" style="left:258px;top:888px">
  <div class="page-brand"><span class="brand-square"></span><div class="brand-name">CINDERMOOR<br>CARE<br>ALLIES</div></div>
  <h2 class="heading" style="top:38px"><span class="accent">Tracking</span><span class="main">&amp; Reporting</span></h2>
  <div class="sub" style="top:62px">Optimizations Completed</div>
  <ul class="list tight" style="top:68px">
    <li>Searchly Analytics and Searchly Console connected</li>
    <li>Call tracking and form submissions live</li>
    <li>Conversion goals configured</li>
    <li>Dashboard access shared</li>
  </ul>
  <div class="sub case" style="top:108px">Next Steps:</div>
  <ul class="list tight" style="top:114px">
    <li>Monitor traffic and lead source data</li>
    <li>Review conversion metrics monthly</li>
  </ul>
  <div class="sub" style="top:107px;left:90px">Next Steps:</div>
  <ul class="list tight" style="top:113px;left:90px">
    <li>Continue monthly citation expansion</li>
    <li>Launch next wave of backlink outreach</li>
  </ul>
  <svg class="chart" viewBox="0 0 160 70" role="img" aria-label="Bar chart of monthly spend and results">
    <g font-family="Poppins, sans-serif" font-size="3.4" fill="#ffffff">
      <path d="M7 66 V22 a4.75 4.75 0 0 1 9.5 0 V66 Z" fill="#1f2a44"/>
      <path d="M22.5 66 V32 a4.75 4.75 0 0 1 9.5 0 V66 Z" fill="#fbb017"/>
      <path d="M38 66 V13 a4.75 4.75 0 0 1 9.5 0 V66 Z" fill="#164d6b"/>
      <path d="M54 66 V40 a4.75 4.75 0 0 1 9.5 0 V66 Z" fill="#fbb017"/>
      <path d="M69 66 V7 a4.75 4.75 0 0 1 9.5 0 V66 Z" fill="#1f2a44"/>
      <path d="M85 66 V26 a4.75 4.75 0 0 1 9.5 0 V66 Z" fill="#fbb017"/>
      <path d="M101 66 V33 a4.75 4.75 0 0 1 9.5 0 V66 Z" fill="#164d6b"/>
      <path d="M116 66 V40 a4.75 4.75 0 0 1 9.5 0 V66 Z" fill="#fbb017"/>
      <path d="M131 66 V30 a4.75 4.75 0 0 1 9.5 0 V66 Z" fill="#1f2a44"/>
      <text transform="translate(13 64) rotate(-90)">$1000.00</text>
      <text transform="translate(28.5 64) rotate(-90)">$1000.00</text>
      <text transform="translate(44 64) rotate(-90)">$1000.00</text>
      <text transform="translate(60 64) rotate(-90)">$10.00</text>
      <text transform="translate(75 64) rotate(-90)">$2000.00</text>
      <text transform="translate(91 64) rotate(-90)">$1500.00</text>
      <text transform="translate(107 64) rotate(-90)">$1800.00</text>
      <text transform="translate(122 64) rotate(-90)">$9.00</text>
      <text transform="translate(137 64) rotate(-90)">$800.00</text>
    </g>
    <line x1="1" y1="66.3" x2="155" y2="66.3" stroke="#1f2a44" stroke-width=".8"/>
  </svg>
  <div class="footer-title">30 DAYS TO <span class="gold">VALUE REPORT</span><br>CINDERMOOR CARE ALLIES</div>
  <svg class="footer-mark" viewBox="0 0 43 19" aria-hidden="true"><path d="M0 0 H43 L25 19 H13 Q14 8 0 0 Z" fill="#fbb017"/></svg>
</section>

<section class="page" style="left:458px;top:888px">
  <div class="page-brand"><span class="brand-square"></span><div class="brand-name">CINDERMOOR<br>CARE<br>ALLIES</div></div>
  <h2 class="heading" style="top:38px"><span class="accent">What’s Next</span><span class="main">Days 31–60</span></h2>
  <div class="sub" style="top:62px">Optimizations Completed</div>
  <ul class="list tight" style="top:68px">
    <li>Continue backlink outreach and citation expansion</li>
    <li>Publish next wave of blog content</li>
    <li>Drive organic traffic growth via SEO</li>
    <li>Launch paid campaigns (if applicable)</li>
    <li>Review analytics data and optimize for conversions</li>
  </ul>
  <div class="sub" style="top:159px">Notes &amp; Recommendations</div>
  <div class="closing" style="top:165px">
    <p>The foundation is in place. The next phase focuses on growth, visibility, and conversions. We’re excited about the direction and look forward to building on this momentum.</p>
    <p style="margin-top:4px"><b>Prepared by:</b> Helena Marsh<br>Head of Client Success | Cindermoor Care Allies</p>
  </div>
  <div class="footer-title">30 DAYS TO <span class="gold">VALUE REPORT</span><br>CINDERMOOR CARE ALLIES</div>
  <svg class="footer-mark" viewBox="0 0 43 19" aria-hidden="true"><path d="M0 0 H43 L25 19 H13 Q14 8 0 0 Z" fill="#fbb017"/></svg>
</section>

</body>
</html>
```